Motorcycle Shop Business Card

New business card for Motorcycle repair and customization shop.Business name: Copper Falcon Chris Morris443-865-5190, 7214 Quarry Lane Bellmoor, MD 20999. www.dale@copperfalconcustoms.example. I uploaded some motorcycle images and logo and a couple of our calendar shoots. They do not have to be used on card just examples of some of our work and past graphic work.
We work on Vantor Brennick and Custom Built Motorcycles.

Looking for front and back design

Target Market(s)

Motorcycle owners

Industry/Entity Type

Motorcycle Part

```html
<!DOCTYPE html>
<html lang="en">
<head>
<meta charset="utf-8">
<title>Copper Falcon Customs – Business Card</title>
<link rel="stylesheet" href="https://fonts.googleapis.com/css2?family=Archivo+Black&family=Arimo:wght@400;700&display=swap">
<style>
  :root {
    --page: #e9e6e2;
    --card-white: #ffffff;
    --brand-red: #e3171d;
    --brand-black: #0d0d0d;
    --bar-grey-light: #9a9a9a;
    --bar-grey-dark: #2e2e2e;
    --ink-white: #ffffff;
    --logo-ink: #111111;
  }
  html, body {
    margin: 0;
    width: 1200px;
    height: 901px;
    overflow: hidden;
    background: var(--page);
  }
  .sheet {
    position: relative;
    width: 1200px;
    height: 901px;
  }
  .card {
    position: absolute;
    left: 250px;
    width: 700px;
    height: 400px;
    box-shadow: 0 6px 18px rgba(0,0,0,0.18);
  }
  .card--back { top: 34px; }
  .card--front { top: 467px; }
  .card svg { display: block; width: 700px; height: 400px; }
  .fill-white { fill: var(--card-white); }
  .fill-red { fill: var(--brand-red); }
  .fill-black { fill: var(--brand-black); }
  .logo-name {
    font-family: "Archivo Black", "Arial Black", sans-serif;
    fill: var(--logo-ink);
  }
  .back-title {
    font-family: "Archivo Black", "Arial Black", sans-serif;
    fill: var(--brand-red);
    font-size: 62px;
  }
  .holder-name {
    font-family: "Archivo Black", "Arial Black", sans-serif;
    fill: var(--brand-red);
    font-size: 34px;
  }
  .holder-role {
    font-family: "Arimo", Arial, sans-serif;
    font-weight: 700;
    fill: var(--ink-white);
    font-size: 19px;
  }
  .contact-line {
    font-family: "Arimo", Arial, sans-serif;
    fill: var(--ink-white);
    font-size: 14px;
  }
  .contact-icon { fill: none; stroke: var(--ink-white); stroke-width: 1.6; stroke-linejoin: round; }
  .contact-icon-solid { fill: var(--ink-white); }
</style>
</head>
<body>
<main class="sheet">

  <section class="card card--back" aria-label="Business card back">
    <svg viewBox="0 0 700 400" xmlns="http://www.w3.org/2000/svg">
      <rect class="fill-white" width="700" height="400"/>
      <polygon class="fill-black" points="0,0 60,0 0,110"/>
      <polygon class="fill-red" points="60,0 330,0 330,280 240,400 30,400 0,330 0,110"/>
      <polygon class="fill-black" points="345,0 700,0 700,400 270,400 345,300"/>
      <polygon class="fill-black" points="0,360 0,400 20,400"/>
      <g class="brand-mark">
        <text class="logo-name" x="175" y="190" text-anchor="middle" font-size="32">Copper Falcon</text>
        <text class="logo-name" x="175" y="228" text-anchor="middle" font-size="21">Customs</text>
      </g>
      <text class="back-title" x="400" y="120">Copper</text>
      <text class="back-title" x="400" y="188">falcon</text>
    </svg>
  </section>

  <section class="card card--front" aria-label="Business card front">
    <svg viewBox="0 0 700 400" xmlns="http://www.w3.org/2000/svg">
      <defs>
        <linearGradient id="roleBarFront" x1="0" y1="0" x2="1" y2="0">
          <stop offset="0" stop-color="var(--bar-grey-light)"/>
          <stop offset="1" stop-color="var(--bar-grey-dark)"/>
        </linearGradient>
      </defs>
      <rect class="fill-white" width="700" height="400"/>
      <polygon class="fill-black" points="0,0 45,0 0,95"/>
      <polygon class="fill-red" points="45,0 300,0 300,290 215,400 55,400 0,300 0,95"/>
      <polygon class="fill-black" points="318,0 700,0 700,400 240,400 318,305"/>
      <polygon class="fill-black" points="0,345 0,400 25,400"/>

      <g class="brand-mark">
        <text class="logo-name" x="155" y="190" text-anchor="middle" font-size="30">Copper Falcon</text>
        <text class="logo-name" x="155" y="226" text-anchor="middle" font-size="20">Customs</text>
      </g>

      <text class="holder-name" x="420" y="128">Dale Fenwick</text>
      <rect x="355" y="146" width="345" height="34" fill="url(#roleBarFront)"/>
      <text class="holder-role" x="540" y="170" text-anchor="middle">proprietor</text>

      <g class="contact">
        <rect class="contact-icon" x="362" y="214" width="16" height="24" rx="3"/>
        <rect class="contact-icon-solid" x="366" y="218" width="8" height="12"/>
        <text class="contact-line" x="392" y="231">410-555-0137, 7214</text>
        <path class="contact-icon-solid" d="M360 276 L370 266 L380 276 L377 276 L377 285 L373 285 L373 279 L367 279 L367 285 L363 285 L363 276 Z"/>
        <text class="contact-line" x="392" y="282">Quarry Lane Bellmoor, MD 20999.</text>
        <rect class="contact-icon" x="361" y="320" width="20" height="14" rx="1"/>
        <path class="contact-icon" d="M361 320 L371 329 L381 320"/>
        <text class="contact-line" x="392" y="332">www.dale@copperfalconcustoms.example</text>
      </g>
    </svg>
  </section>

</main>
</body>
</html>
```